Halvet Energy Letter Head- with all subsidiaries

We need a letterhead that will showcase all Halvet Energy subsidiaries, while still have Halvet Energy logo ontop.

```html
<!DOCTYPE html>
<html lang="en">
<head>
<meta charset="utf-8">
<title>Halvet Energy Letterhead</title>
<link href="https://fonts.googleapis.com/css2?family=Open+Sans:wght@400;600;700&display=swap" rel="stylesheet">
<style>
  :root {
    --backdrop: #e4e4e4;
    --paper: #ffffff;
    --ink: #454547;
    --ink-strong: #2e2e30;
    --gold: #c6aa66;
    --charcoal: #3f3f41;
  }
  * { box-sizing: border-box; margin: 0; padding: 0; }
  html, body {
    width: 1040px; height: 1200px; overflow: hidden;
    background: var(--backdrop);
    font-family: "Open Sans", Arial, sans-serif;
    color: var(--ink);
  }
  .letterhead {
    position: absolute; left: 69px; top: 20px;
    width: 902px; height: 1160px;
    background: var(--paper);
    box-shadow: 0 2px 10px rgba(0,0,0,0.12);
    overflow: hidden;
  }
  .brand {
    position: absolute; left: 86px; top: 70px;
    display: flex; align-items: center; gap: 12px;
  }
  .brand-mark { width: 34px; height: 34px; background: var(--gold); }
  .brand-name {
    font-size: 34px; font-weight: 700; color: var(--charcoal);
    letter-spacing: 0.5px;
  }
  .contact {
    position: absolute; right: 92px; top: 76px;
    list-style: none; text-align: right;
    font-size: 14.5px; line-height: 17.5px; color: var(--ink-strong);
  }
  .contact li { display: flex; justify-content: flex-end; align-items: center; gap: 6px; }
  .contact svg { width: 11px; height: 11px; fill: var(--ink-strong); }
  .letter-body {
    position: absolute; left: 86px; top: 208px; width: 728px;
    font-size: 14.6px; line-height: 17.5px;
  }
  .issue-date { margin-bottom: 17px; }
  .recipient { margin-bottom: 49px; }
  .salutation { margin-bottom: 26px; }
  .letter-body p.copy {
    line-height: 26.3px; text-align: justify; margin-bottom: 26px;
  }
  .closing { margin-top: 44px; }
  .signatory {
    margin-top: 62px; font-size: 19px; font-weight: 600;
    color: var(--ink-strong); line-height: 24px;
  }
  .signatory-role { margin-top: 6px; }
  .subsidiaries {
    position: absolute; left: 80px; top: 1016px; width: 740px;
    display: grid; grid-template-columns: repeat(6, 1fr);
    list-style: none; align-items: center;
  }
  .subsidiary {
    display: flex; align-items: center; justify-content: center; gap: 5px;
    font-size: 11.5px; font-weight: 700; color: var(--charcoal);
    white-space: nowrap;
  }
  .subsidiary .dot { width: 9px; height: 9px; background: var(--gold); flex: none; }
  .footer-wave { position: absolute; left: 0; bottom: 0; width: 902px; height: 109px; }
</style>
</head>
<body>
<main class="letterhead">
  <header>
    <div class="brand">
      <span class="brand-mark"></span>
      <span class="brand-name">Halvet Energy</span>
    </div>
    <ul class="contact">
      <li>044-555 018 240
        <svg viewBox="0 0 12 12"><path d="M1 4c0-2 2-3 5-3s5 1 5 3l-2 1-1-2H4L3 5 1 4zM3 6h6l1 5H2z"/></svg></li>
      <li>info@halvetenergy.com
        <svg viewBox="0 0 12 12"><path d="M0 2h12v8H0zM1 3l5 4 5-4"/></svg></li>
      <li>www.halvetenergy.com
        <svg viewBox="0 0 12 12"><circle cx="6" cy="6" r="5.5"/></svg></li>
    </ul>
  </header>

  <section class="letter-body">
    <p class="issue-date">Issuing Date: May 5, 2018</p>
    <p class="recipient">Name Of Employee Mr. XYZABC<br>Address of Employee<br>Address Line 2 etc..</p>
    <p class="salutation">Dear Mr.XYZABC</p>
    <p class="copy">Lorem Ipsum has been the industry's standard dummy text ever since the 1500s, when an unknown printer took a galley of type and scrambled it to make a type specimen book. It has survived not only five centuries, but also the leap into electronic typesetting, remaining essentially unchanged. It was popularised in the 1960s with the release of Letraset sheets containing Lorem Ipsum passages, and more recently with desktop publishing software like Aldus PageMaker including versions of Lorem Ipsum.</p>
    <p class="copy">Lorem Ipsum is simply dummy text of the printing and typesetting industry. Lorem Ipsum has been the industry's standard dummy text ever since the 1500s, when an unknown printer took a galley of type and scrambled it to make a type specimen book.</p>
    <p class="copy">It has survived not only five centuries, but also the leap into electronic typesetting, remaining essentially unchanged. It was popularised in the 1960s with the release of Letraset sheets containing Lorem IpsumIpsum passages.</p>
    <p class="closing">Yours Sincerely</p>
    <p class="signatory">Jonah Whitfield</p>
    <p class="signatory-role">Managing Director</p>
  </section>

  <ul class="subsidiaries">
    <li class="subsidiary"><span class="dot"></span>Norvane Electric</li>
    <li class="subsidiary"><span class="dot"></span>Brightline Electrical</li>
    <li class="subsidiary"><span class="dot"></span>Halvet Logistics</li>
    <li class="subsidiary"><span class="dot"></span>Halvet Caribbean</li>
    <li class="subsidiary"><span class="dot"></span>Halvet Aviation</li>
    <li class="subsidiary"><span class="dot"></span>Halvet Acquisitions</li>
  </ul>

  <svg class="footer-wave" viewBox="0 920 789 95" preserveAspectRatio="none" aria-hidden="true">
    <path fill="var(--gold)" d="M0 928 C60 962 180 988 300 984 C380 980 430 968 475 958 C380 990 200 1008 0 962 Z"/>
    <path fill="var(--charcoal)" d="M0 972 C150 1012 330 1002 480 966 C610 936 720 934 789 942 L789 1015 L0 1015 Z"/>
  </svg>
</main>
</body>
</html>
```